Commercial and Residential Paint Contractor needs website

We need a website for our residential painting, multi-family painting and commercial painting company. We paint interior and exterior of houses, apartments and commercial buildings. I would like an about us page, residential page, multi family page, commercial page and contact us. Need keywords added to website for seo opitimazation. I like this website https://www.velmorandhalestudio.com/

Target Market(s)

General Contractors and commercial property managers

Coding

Coded - Design and coding required

Number of Pages Required

5+ page

Font styles to use
Sans Serif

Requirements
Must have
• I need SEO keywords on pages

```html
<!DOCTYPE html>
<html lang="en">
<head>
<meta charset="utf-8">
<title>Halcrest Painting – Commercial, Multi-Family &amp; Residential Painters</title>
<meta name="description" content="Halcrest Painting: commercial painting, apartment and multi-family painting, residential interior and exterior painting contractor in the DFW area.">
<link rel="stylesheet" href="https://fonts.googleapis.com/css2?family=Ubuntu:wght@400;500;700&family=Lato:ital,wght@0,400;0,700;1,400&family=Open+Sans:wght@800&display=swap">
<style>
:root{
  --blue:#134b91;
  --blue-dark:#0d3a75;
  --red:#c8202f;
  --ink:#222;
  --muted:#7a7a7a;
  --light:#f6f6f6;
  --line:#e6e6e6;
  --white:#fff;
  --footer:#1d2420;
  --grad:linear-gradient(90deg,var(--red),var(--blue));
}
*{box-sizing:border-box;margin:0;padding:0}
html,body{width:1200px;height:3484px;overflow:hidden}
body{position:relative;background:var(--white);font-family:"Lato",sans-serif;color:var(--ink)}
h1,h2,h3{font-family:"Ubuntu",sans-serif;font-weight:400}
.btn{position:absolute;display:flex;align-items:center;justify-content:center;border-radius:22px;background:var(--grad);color:var(--white);font-family:"Ubuntu",sans-serif;font-weight:500;font-size:13px;text-decoration:none}
.section-title{position:absolute;left:0;width:1200px;text-align:center;font-size:31px;color:var(--ink)}
.dots{position:absolute;left:0;width:1200px;display:flex;justify-content:center;align-items:center;gap:12px}
.dot{width:7px;height:7px;border-radius:50%;background:#222}
.dot.active{width:16px;height:16px;border:2px solid var(--red);background:radial-gradient(var(--red) 35%,transparent 40%)}

/* header */
.site-header{position:absolute;left:0;top:0;width:1200px;height:135px;background:var(--white)}
.brand{position:absolute;left:162px;top:38px;display:flex;align-items:center;gap:10px;font-family:"Ubuntu",sans-serif;font-weight:700;font-size:38px;color:var(--blue);letter-spacing:1px}
.brand-mark{width:22px;height:22px;background:var(--red)}
.call-bar{position:absolute;left:706px;top:17px;width:336px;height:36px;background:var(--red);border-radius:3px;display:flex;align-items:center;justify-content:center;gap:7px;color:var(--white);font-family:"Ubuntu",sans-serif;font-weight:700;font-size:15px}
.main-nav{position:absolute;left:647px;top:77px;display:flex;align-items:center;gap:6px;font-family:"Lato",sans-serif;font-size:14px;color:#333}
.main-nav a{color:#333;text-decoration:none;padding:8px 12px;border-radius:18px}
.main-nav a.current{background:var(--grad);color:var(--white);padding:8px 18px}

/* hero */
.hero{position:absolute;left:0;top:135px;width:1200px;height:525px}
.hero-photo{position:absolute;inset:0;background:linear-gradient(90deg,#6fb0df 0%,#9fcde8 22%,#cfd3d6 45%,#e2e2e0 70%,#d6d4d1 100%)}
.hero-copy{position:absolute;left:656px;top:140px}
.hero-copy .welcome{font-family:"Ubuntu",sans-serif;font-size:32px;color:var(--blue)}
.hero-copy .big{display:block;font-family:"Open Sans",sans-serif;font-weight:800;font-size:72px;line-height:78px;letter-spacing:1px}
.hero-copy .big.white{color:var(--white)}
.hero-copy .big.red{color:var(--red)}

/* about */
.about{position:absolute;left:0;top:660px;width:1200px;height:456px;background:var(--white)}
.about h2{position:absolute;left:161px;top:90px;font-size:31px}
.about p{position:absolute;left:161px;width:422px;font-size:11.5px;line-height:20.5px;color:var(--muted)}
.about-frame-blue{position:absolute;left:672px;top:80px;width:366px;height:248px;background:var(--blue)}
.about-photo{position:absolute;left:620px;top:114px;width:395px;height:266px;background:linear-gradient(110deg,#e9eef1 0%,#f3f4f2 45%,#cfe4a8 75%,#a6d264 100%)}
.about-frame-red{position:absolute;left:605px;top:129px;width:393px;height:266px;border:1.5px solid var(--red)}

/* services */
.services{position:absolute;left:0;top:1116px;width:1200px;height:575px;background:var(--light)}
.service-card{position:absolute;top:122px;width:278px;height:369px;background:var(--white);border:1px solid #ececec;border-radius:4px;text-align:center}
.service-card .img{height:211px;border-radius:4px 4px 0 0}
.service-card h3{margin-top:19px;font-size:18px;color:var(--ink)}
.service-card p{margin:9px auto 0;width:200px;font-size:11.5px;line-height:20.5px;color:var(--muted)}
.service-card .btn{left:50%;transform:translateX(-50%);top:342px;width:128px;height:41px}

/* gallery */
.gallery{position:absolute;left:0;top:1691px;width:1200px;height:622px}
.gallery .shot{position:absolute;top:125px;height:397px;border-radius:3px}

/* estimate */
.estimate{position:absolute;left:0;top:2313px;width:1200px;height:417px;background:#f2f2f2}
.estimate-art{position:absolute;left:0;top:0;width:507px;height:417px;background:linear-gradient(160deg,#f4f1ea 0%,#e9dcc4 40%,#cfe6f3 70%,#f1f1f1 100%)}
.estimate-panel{position:absolute;left:507px;top:0;width:531px;height:417px;background:var(--blue)}
.estimate-panel h2{position:absolute;left:0;width:531px;top:55px;text-align:center;color:var(--white);font-size:31px;font-weight:500}
.field{position:absolute;border:1.5px solid var(--white);border-radius:20px;color:var(--white);font-style:italic;font-size:11.5px;padding:0 18px;display:flex;align-items:center}
.field.area{align-items:flex-start;padding-top:12px;border-radius:16px}
.submit{position:absolute;left:202px;top:320px;width:127px;height:40px;border-radius:20px;background:var(--white);color:var(--ink);font-family:"Ubuntu",sans-serif;font-weight:500;font-size:13px;display:flex;align-items:center;justify-content:center}

/* testimonials */
.reviews{position:absolute;left:0;top:2730px;width:1200px;height:460px}
.review{position:absolute;top:138px;width:279px;height:230px;background:var(--white);box-shadow:0 2px 10px rgba(0,0,0,.06)}
.quote{position:absolute;font-family:"Open Sans",sans-serif;font-weight:800;font-size:52px;line-height:44px;color:var(--red)}
.quote.open{left:22px;top:-12px}
.quote.close{right:22px;bottom:-26px}
.review .role{position:absolute;left:25px;top:36px;font-size:11.5px;color:var(--blue)}
.review .name{position:absolute;left:25px;top:52px;font-family:"Ubuntu",sans-serif;font-size:14px}
.review .stars{position:absolute;right:18px;top:33px;color:#f27b1b;font-size:13px;letter-spacing:-1px}
.review p{position:absolute;left:25px;top:85px;width:235px;font-size:11.5px;line-height:20.5px;color:var(--muted)}

/* footer */
.site-footer{position:absolute;left:0;top:3190px;width:1200px;height:294px;background:radial-gradient(ellipse at 40% 30%,#3d4a3a 0%,#252c27 55%,var(--footer) 100%)}
.footer-brand{position:absolute;left:0;width:1200px;top:64px;display:flex;justify-content:center;align-items:center;gap:10px;font-family:"Ubuntu",sans-serif;font-weight:700;font-size:36px;color:var(--white);letter-spacing:1px}
.footer-nav{position:absolute;left:0;width:1200px;top:163px;display:flex;justify-content:center;gap:24px;font-size:13px;color:var(--white)}
.footer-contact{position:absolute;left:0;width:1200px;top:195px;display:flex;justify-content:center;gap:16px;font-size:11.5px;color:var(--white)}
.footer-contact span{display:flex;align-items:center;gap:7px}
.footer-rule{position:absolute;left:161px;width:878px;top:253px;height:1px;background:rgba(255,255,255,.15)}
.copyright{position:absolute;left:0;width:1200px;top:268px;text-align:center;font-size:10px;color:var(--white)}
</style>
</head>
<body>

<header class="site-header">
  <div class="brand"><span class="brand-mark"></span>HALCREST PAINTING</div>
  <div class="call-bar">
    <svg width="13" height="13" viewBox="0 0 24 24"><path fill="#fff" d="M6.6 10.8a15 15 0 0 0 6.6 6.6l2.2-2.2c.3-.3.7-.4 1-.2 1.1.4 2.3.6 3.6.6.6 0 1 .4 1 1V20c0 .6-.4 1-1 1A17 17 0 0 1 3 4c0-.6.4-1 1-1h3.5c.6 0 1 .4 1 1 0 1.3.2 2.5.6 3.6.1.3 0 .7-.2 1z"/></svg>
    CALL OUR OFFICE: 555-210-4836
  </div>
  <nav class="main-nav">
    <a class="current" href="#">Home</a>
    <a href="#">About Us</a>
    <a href="#">Services</a>
    <a href="#">Gallery</a>
    <a href="#">Contact Us</a>
    <svg width="14" height="14" viewBox="0 0 24 24" style="margin-left:12px"><circle cx="10" cy="10" r="6.5" fill="none" stroke="#222" stroke-width="3"/><line x1="15" y1="15" x2="21" y2="21" stroke="#222" stroke-width="3.5" stroke-linecap="round"/></svg>
  </nav>
</header>

<section class="hero">
  <div class="hero-photo" role="img" aria-label="Painter holding paintbrushes in an empty bright room being prepared for painting"></div>
  <div class="hero-copy">
    <div class="welcome">Welcome To</div>
    <h1><span class="big white">HALCREST</span><span class="big red">PAINTING</span></h1>
  </div>
  <a class="btn" style="left:656px;top:341px;width:127px;height:41px" href="#">Get An Estimate</a>
  <div class="dots" style="top:489px"><span class="dot"></span><span class="dot active"></span><span class="dot"></span></div>
</section>

<section class="about">
  <h2>About Us</h2>
  <p style="top:136px">We are family owned and operated with over 10 years' experience. We pride our self in performing to the highest degree of workmanship standards. Halcrest Painting is your best choice for commercial, residential and multi-family painting in the DFW/Fort Worth area.</p>
  <p style="top:237px">Our experienced estimators will meet with you and customize a proposal to meet your needs. They will stay with you from the beginning of the project to the end, making sure you are 100% satisfied. If you are looking for a dependable painter call our office 555-210-4836.</p>
  <a class="btn" style="left:161px;top:341px;width:127px;height:41px" href="#">Read More</a>
  <div class="about-frame-blue"></div>
  <div class="about-photo" role="img" aria-label="Smiling painter rolling green paint onto a white wall"></div>
  <div class="about-frame-red"></div>
</section>

<section class="services">
  <h2 class="section-title" style="top:64px">Our Services</h2>
  <article class="service-card" style="left:184px">
    <div class="img" role="img" aria-label="Row of apartment buildings painted in bright multi-colour blocks" style="background:linear-gradient(90deg,#b9784c,#e6c13a 40%,#3a7fd1 75%,#2f6db8)"></div>
    <h3>Apartment Painting</h3>
    <p>There are many variations of passages of painting services available, but the majority.</p>
    <a class="btn" href="#">Read More</a>
  </article>
  <article class="service-card" style="left:483px">
    <div class="img" role="img" aria-label="Modern commercial office lounge with colourful painted booths" style="background:linear-gradient(180deg,#d9d6cf,#7e8a6a 55%,#4a5a3c)"></div>
    <h3>Commercial Painting</h3>
    <p>There are many variations of passages of painting services available, but the majority.</p>
    <a class="btn" href="#">Read More</a>
  </article>
  <article class="service-card" style="left:783px">
    <div class="img" role="img" aria-label="Two-storey house exterior with ladders and paint cans during repainting" style="background:linear-gradient(180deg,#8fb9e0,#e8e4dd 50%,#cfc8bc)"></div>
    <h3>Residential Painting</h3>
    <p>There are many variations of passages of painting services available, but the majority.</p>
    <a class="btn" href="#">Read More</a>
  </article>
</section>

<section class="gallery">
  <h2 class="section-title" style="top:56px">Our Gallery</h2>
  <div class="shot" style="left:0;width:237px;background:linear-gradient(90deg,#d8d6d2,#6c6a66 55%,#c9c6c0)" role="img" aria-label="Interior wall and stone column with painting supplies on a counter"></div>
  <div class="shot" style="left:311px;width:578px;background:linear-gradient(180deg,#ece9e4,#f4f2ee 45%,#d8d2c8 75%,#8b7056)" role="img" aria-label="Freshly painted white kitchen with island and pendant light"></div>
  <div class="shot" style="left:963px;width:237px;background:linear-gradient(180deg,#1f62c4 0%,#3a78d0 30%,#9b8c7c 60%,#bfae98 100%)" role="img" aria-label="Brick house exterior under a blue sky"></div>
  <div class="dots" style="top:552px"><span class="dot"></span><span class="dot active"></span><span class="dot"></span></div>
</section>

<section class="estimate">
  <div class="estimate-art" role="img" aria-label="Cheerful painter with a paint roller leaning on a wooden ladder among colourful confetti"></div>
  <div class="estimate-panel">
    <h2>Get Free Estimate</h2>
    <div class="field" style="left:52px;top:110px;width:208px;height:37px">Your Name*</div>
    <div class="field" style="left:271px;top:110px;width:208px;height:37px">Your Phone*</div>
    <div class="field" style="left:52px;top:159px;width:208px;height:36px">Your Email*</div>
    <div class="field" style="left:271px;top:159px;width:208px;height:36px">Your Subject*</div>
    <div class="field area" style="left:52px;top:208px;width:427px;height:86px">Your Message</div>
    <div class="submit">Submit</div>
  </div>
</section>

<section class="reviews">
  <h2 class="section-title" style="top:64px">What Our Client Say</h2>
  <article class="review" style="left:161px">
    <span class="quote open">&ldquo;</span>
    <span class="role">Client</span><span class="stars">★★★★★</span>
    <span class="name">Nolan Pryce</span>
    <p>Lorem ipsum dolor sit amet, consectetur adipisicing elit, sed do eiusmod tempor incididunt ut labore et dolore magna aliqua. Ut enim ad minim veniam, quis nostrud exercitation ullamco laboris nisi ut aliquip. ex ea commodo consequat.</p>
    <span class="quote close">&rdquo;</span>
  </article>
  <article class="review" style="left:461px">
    <span class="quote open">&ldquo;</span>
    <span class="role">Client</span><span class="stars">★★★★★</span>
    <span class="name">Tessa Marlowe</span>
    <p>Lorem ipsum dolor sit amet, consectetur adipisicing elit, sed do eiusmod tempor incididunt ut labore et dolore magna aliqua. Ut enim ad minim veniam, quis nostrud exercitation ullamco laboris nisi ut aliquip. ex ea commodo consequat.</p>
    <span class="quote close">&rdquo;</span>
  </article>
  <article class="review" style="left:760px">
    <span class="quote open">&ldquo;</span>
    <span class="role">Client</span><span class="stars">★★★★★</span>
    <span class="name">Idris Kemble</span>
    <p>Lorem ipsum dolor sit amet, consectetur adipisicing elit, sed do eiusmod tempor incididunt ut labore et dolore magna aliqua. Ut enim ad minim veniam, quis nostrud exercitation ullamco laboris nisi ut aliquip. ex ea commodo consequat.</p>
    <span class="quote close">&rdquo;</span>
  </article>
  <div class="dots" style="top:399px;gap:9px"><span class="dot" style="width:5px;height:5px"></span><span class="dot" style="width:8px;height:8px"></span><span class="dot" style="width:5px;height:5px"></span></div>
</section>

<footer class="site-footer">
  <div class="footer-brand"><span class="brand-mark"></span>HALCREST PAINTING</div>
  <nav class="footer-nav"><span>Home</span><span>About Us</span><span>Services</span><span>Gallery</span><span>Contact Us</span></nav>
  <div class="footer-contact">
    <span><svg width="11" height="11" viewBox="0 0 24 24"><path fill="#fff" d="M6.6 10.8a15 15 0 0 0 6.6 6.6l2.2-2.2c.3-.3.7-.4 1-.2 1.1.4 2.3.6 3.6.6.6 0 1 .4 1 1V20c0 .6-.4 1-1 1A17 17 0 0 1 3 4c0-.6.4-1 1-1h3.5c.6 0 1 .4 1 1 0 1.3.2 2.5.6 3.6.1.3 0 .7-.2 1z"/></svg>555-210-4836</span>
    <span><svg width="12" height="10" viewBox="0 0 24 18"><rect x="0" y="0" width="24" height="18" rx="2" fill="#fff"/><path d="M1 2 L12 10 L23 2" fill="none" stroke="#1d2420" stroke-width="2"/></svg>info@example.com</span>
    <span><svg width="9" height="12" viewBox="0 0 18 24"><path fill="#fff" d="M9 0a9 9 0 0 0-9 9c0 7 9 15 9 15s9-8 9-15a9 9 0 0 0-9-9zm0 12.5A3.5 3.5 0 1 1 9 5.5a3.5 3.5 0 0 1 0 7z"/></svg>12345 ABC Ave. 4567 City, AB 12345</span>
  </div>
  <div class="footer-rule"></div>
  <div class="copyright">Copyright © 2020 Halcrest Painting &nbsp;|&nbsp; All Rights Reserved.</div>
</footer>

</body>
</html>
```